QUORVIX - Sydney Based Technology Consultancy -Logo & Business Card design

Who are we?
-
Quorvix is an emerging and advanced technology consulting and professional services business based in Sydney, Australia. Quorvix specialising in increasing value to organisations through the effective use of current and emerging technologies, ensuring that technology is a sustainable catalyst to attaining stated business goals.

We pride ourselves in challenging the norm.

What do we want?
-
We are looking to update our "Brand" we already have a simple “home grown” logo and we are now looking for a new one, once we have this updated logo and businesses look and feel though the business card design we will refresh our website with the new logo and design thus updating the Companies overall look at feel.

Our current site is www.quorvix-example.net.au is a very basic wordpress site and we will be updating it once we have the new logo and designs done

Our initial thoughts on the new Quorvix identity are
• Logo Concept
- One of the key things is obviously the 8
- I was thinking that a logo that had 8 as the core of the logo would be cool,
- Almost like having a “ring” or hoop that is twisted to form an 8 with different services scribed on the inside.
- So we would have a Large 8 and the inside would have ring each service or section engraved.

• Brand / web Feel
- Simple
- Professional
- Innovative
- Clear
- Destination
- Unique
- Impartial
- Safe
- Leading edge
- Familiar

- Emerging technologies
- White and ice / glacier blue
- The familiar feel of the Brindle web site
- Embedded specialist Video clips

• Portfolio of Services
- Quorvix – A smart place for Smart people
- Quorvix – we provide the process to take ideas from awareness to reality
- Focus should be on the brand quality consistent clear local knowledge with regional, national, theatre and global presence

Access to Specialists
- Emerging technologies
- Sustainability
- Collaboration
- Data centre
- Virtualisation

• Adjacent ideas under the one Brand
- Tembrosk – Enable Business Collaboration
- Plinsk – Infrastructure Virtualisation
- morvo - smart people and processes
- skandel - Emerging technologies
- brunhavel - business to technology integration
- tolpin - Smart Infrastructure
- yusk – Connected communities
- dwol - sustainability

Target Market(s)

Australia, New Zealand and Asia pacific organisations that are typically English speaking.
Markets
- IT & Technology partners
- Banking and Finance
- Health

Industry/Entity Type

Business

Requirements
Must have
• Logo
Business cards
Colour pallette
3D Logo
Nice to have
• Style guide
Designer who can also assist with new Wordpress design
Should not have
• we don't want cheap looking, overtly flashy or gimmicky logo.

```html
<!DOCTYPE html>
<html lang="en">
<head>
<meta charset="utf-8">
<title>Quorvix – Business Card</title>
<link rel="stylesheet" href="https://fonts.googleapis.com/css2?family=Fredoka:wght@600&display=swap">
<style>
  :root {
    --page: #ffffff;
    --card-edge: #3a3640;
    --violet-deep: #5d5569;
    --violet-mid: #8f859d;
    --violet-soft: #b9b2c3;
    --glow: #f4f3f6;
    --ink-white: #ffffff;
    --brand-ink: #5a5366;
  }
  html, body {
    margin: 0;
    padding: 0;
    width: 1200px;
    height: 572px;
    overflow: hidden;
    background: var(--page);
  }
  .canvas {
    display: block;
    width: 1200px;
    height: 572px;
  }
  .card-text {
    font-family: "Fredoka", "Arial Rounded MT Bold", sans-serif;
    font-weight: 600;
    fill: var(--ink-white);
    font-size: 42px;
  }
  .brand-name {
    font-family: "Fredoka", "Arial Rounded MT Bold", sans-serif;
    font-weight: 600;
    fill: var(--brand-ink);
    font-size: 54px;
    letter-spacing: 1px;
  }
</style>
</head>
<body>
<svg class="canvas" viewBox="0 0 1200 572" xmlns="http://www.w3.org/2000/svg" role="img" aria-label="Quorvix business card">
  <defs>
    <linearGradient id="card-fill" x1="0" y1="0" x2="1" y2="0">
      <stop offset="0" style="stop-color: var(--violet-deep)"/>
      <stop offset="0.45" style="stop-color: var(--violet-mid)"/>
      <stop offset="1" style="stop-color: var(--violet-soft)"/>
    </linearGradient>
    <radialGradient id="card-glow" cx="930" cy="140" r="360" gradientUnits="userSpaceOnUse">
      <stop offset="0" style="stop-color: var(--glow); stop-opacity: 1"/>
      <stop offset="0.5" style="stop-color: var(--glow); stop-opacity: 0.45"/>
      <stop offset="1" style="stop-color: var(--glow); stop-opacity: 0"/>
    </radialGradient>
    <linearGradient id="rail-fill" x1="0" y1="0" x2="1" y2="0">
      <stop offset="0" style="stop-color: var(--violet-deep)"/>
      <stop offset="0.6" style="stop-color: var(--violet-mid)"/>
      <stop offset="1" style="stop-color: var(--ink-white)"/>
    </linearGradient>
    <radialGradient id="bead-fill" cx="0.4" cy="0.35" r="0.7">
      <stop offset="0" style="stop-color: var(--ink-white)"/>
      <stop offset="0.6" style="stop-color: var(--violet-soft)"/>
      <stop offset="1" style="stop-color: var(--violet-deep)"/>
    </radialGradient>
    <clipPath id="card-clip">
      <rect x="102" y="50" width="999" height="500"/>
    </clipPath>
  </defs>

  <g class="card">
    <rect class="card-base" x="102" y="50" width="999" height="500" fill="url(#card-fill)"/>
    <rect class="card-glow" x="102" y="50" width="999" height="500" fill="url(#card-glow)"/>

    <circle class="corner-ring" cx="208" cy="114" r="104" fill="none" stroke="var(--ink-white)" stroke-width="7" clip-path="url(#card-clip)"/>

    <g class="brand-mark">
      <text class="brand-name" x="745" y="200">QUORVIX</text>
      <circle class="brand-dot" cx="1000" cy="150" r="22" fill="var(--brand-ink)"/>
    </g>

    <g class="rails">
      <rect class="rail rail-upper" x="360" y="254" width="665" height="6" fill="url(#rail-fill)"/>
      <rect class="rail rail-lower" x="575" y="283" width="451" height="6" fill="url(#rail-fill)"/>
      <circle class="rail-bead" cx="986" cy="273" r="22" fill="url(#bead-fill)"/>
    </g>

    <g class="details">
      <text class="card-text" x="173" y="324">Some text</text>
      <text class="card-text" x="173" y="380">Some text</text>
      <text class="card-text" x="173" y="432">Some text</text>
      <text class="card-text" x="173" y="487">Some text</text>
      <text class="card-text" x="417" y="436">Some text</text>
      <text class="card-text" x="417" y="492">Some text</text>
    </g>

    <rect class="card-edge" x="102.5" y="50.5" width="998" height="499" fill="none" stroke="var(--card-edge)" stroke-width="1"/>
  </g>
</svg>
</body>
</html>
```